Non-profit organization requires InDesign based template for a educational booklet

***Overview***
Our business "The Coastal Brightpath Centre for Skills and Learning" is a not for profit organisation working in vocational education both in the Australian and international markets. While we work within many professional contexts, we also work with projects in developing countries assisting to build institutional capacity in the education industry, upskilling in disadvantaged communities to ultimately facilitate positive development outcomes.

Our project is looking to deliver agricultural-based education units that will be delivered in booklet form. Vocational students will use these unit booklets for self-paced or classroom group study. The front of each unit will have a nice graphical cover page, contents and details about learning in the unit. This will be followed by about 15 pages of educational content with plenty of pictures and other material such as tables and graphs to illustrate learning points. This will then be followed by a short question sheet with space for students to write answers, followed by Activity sheets where students put into practice skills from the unit.

***The designed template should have***
* Cover page;
* Content page;
* Two (2) different introduction pages (two for variation);
* Three (3) different pages for lesson text – these pages will be the main study pages for the students, 3 for variation;
* Activity page - like an activity worksheet;
* Question page - page with questions or reflections that the students need to answer - a space under each question for students to write;

***Design preferences***

*Font – an inDesign default font please like Calibri – text built on a base Normal font 11pt, then headings H1, H2 etc... from that basis e.g. 24pt for H1 etc... the size up to the designer.

Happy to see creativity of graphic artists with the above themes.

Target Market(s)

In the requested project, I require an Adobe InDesign template (file in .indd) to be designed that will have particular characteristics suited to students who are:

* Age 15-17;
* Have the educational equivalent to Australian and US education standard of Yr 8;
* Attending vocational school - vocational schools are between secondary high school and University and are usually used to produce graduates within the skill trade area;
* Agricultural theme in the template;
* Sustainability theme (agricultural sustainability) as well;

Students are from very poor rural farming families in growing rice, coconut, rambutan, mangoes, cocoa, palm oil... - very SE Asian agricultural landscape.

Students are used to black and white government textbooks which are very dry, largely dull in design and colour – we do not want this!

Industry/Entity Type

Agriculture

Font styles to use
Sans Serif

Colors

Designer to choose colors to be used in the design.

Requirements
Must have
• * Final file must be in an editable Adobe Indesign file (.indd), with editable layers;
• * SE Asian agricultural theme in the template;
• * design must not look like dull and boring textbooks or corporate training booklets; * design should be vibrant and interesting but also not distracting from the lesson (i.e. it is not too garish);
• * suitable colours (it will be printed full colour) easy on the eye for students of the age group - colours related to agriculture;
• *Modern look and feel;
Should not have
• * design must not look like dull and boring textbooks or corporate training booklets;

```html
<!DOCTYPE html>
<html lang="en">
<head>
<meta charset="utf-8">
<title>Unit Booklet – Activity Worksheet and Questions</title>
<link href="https://fonts.googleapis.com/css2?family=Raleway:wght@300;400;700;900&display=swap" rel="stylesheet">
<style>
  :root{
    --stage:#000;
    --paper:#fff;
    --accent:#fbb813;
    --ink:#111;
    --rule:#d9d9d9;
    --muted:#8a8a8a;
    --field-a:#8a5a2c;
    --field-b:#c27a3a;
    --sky-a:#5f6c63;
    --sky-b:#a59f86;
    --wood-a:#b89f87;
    --wood-b:#9c8570;
  }
  *{box-sizing:border-box;margin:0;padding:0}
  html,body{width:914px;height:1200px;overflow:hidden;background:var(--stage)}
  body{position:relative;font-family:"Raleway",sans-serif;color:var(--ink)}

  .spread{position:absolute;left:67px;width:781px;height:552px;overflow:hidden;background:var(--paper)}
  .spread--activity{top:34px}
  .spread--questions{top:610px;left:70px;width:779px;height:551px}

  .masthead{position:absolute;left:22px;right:22px;top:24px;display:flex;align-items:center;gap:10px;z-index:3}
  .masthead__name{font-weight:700;font-size:8.5px;color:var(--accent);white-space:nowrap}
  .masthead__rule{flex:1;height:1px;background:var(--accent);opacity:.8}
  .masthead__edition{font-size:5px;color:#e8e3d0;letter-spacing:.5px;white-space:nowrap}

  .hero{position:absolute;left:0;top:0;width:100%;height:166px;
    background:linear-gradient(180deg,var(--sky-a) 0%,var(--sky-b) 38%,#3d4a2e 48%,var(--field-a) 56%,var(--field-b) 100%)}
  .title{position:absolute;left:25px;font-weight:900;color:#fff;white-space:nowrap;letter-spacing:-1px;z-index:2}
  .title--activity{top:118px;font-size:78px;line-height:1}
  .title--questions{top:76px;left:23px;font-size:60px;line-height:1}

  .task{position:absolute;width:330px;height:70px}
  .task__num{position:absolute;left:0;top:0;width:42px;font-weight:400;font-size:42px;line-height:1;padding-top:7px;letter-spacing:-1px}
  .task__num::before,.task__num::after{content:"";position:absolute;left:0;width:32px;height:4px;background:var(--accent)}
  .task__num::before{top:0}
  .task__num::after{top:53px}
  .task__label{position:absolute;left:74px;top:-4px;font-weight:700;font-size:6.2px;letter-spacing:.1px;padding-left:14px;white-space:nowrap}
  .task__label::before{content:"";position:absolute;left:0;top:3px;width:10px;height:2px;background:var(--accent)}
  .task__lines{position:absolute;left:74px;top:9px;width:254px;height:45px;
    background:repeating-linear-gradient(180deg,transparent 0 13px,var(--rule) 13px 14px)}

  .footer{position:absolute;bottom:12px;display:flex;align-items:center;gap:8px;font-size:4.5px;color:var(--muted)}
  .footer__name{color:var(--accent);font-weight:700;font-size:5px}
  .footer__dot{width:3px;height:3px;background:var(--accent)}
  .footer--left{left:22px}
  .footer--right{right:22px}

  .wood{position:absolute;inset:0;
    background:linear-gradient(90deg,var(--wood-a) 0%,var(--wood-b) 20%,var(--wood-a) 40%,#a89077 60%,var(--wood-a) 80%,var(--wood-b) 100%)}
  .spread--questions .masthead__edition{color:#5a4a3a}

  .answer{position:absolute;width:330px;height:62px;background:var(--paper);display:flex}
  .answer__icon{width:48px;height:62px;background:var(--accent);flex:none}
  .answer__lines{position:absolute;left:62px;right:16px;top:2px;height:46px;
    background:repeating-linear-gradient(180deg,transparent 0 13px,var(--rule) 13px 14px)}
</style>
</head>
<body>

<section class="spread spread--activity">
  <div class="hero" role="img" aria-label="Harvested wheat field with round hay bales under a cloudy sky"></div>
  <header class="masthead">
    <span class="masthead__name">The Coastal Brightpath Centre for Skills and Learning</span>
    <span class="masthead__rule"></span>
    <span class="masthead__edition">EDITION 1 | 2018</span>
  </header>
  <h1 class="title title--activity">Activity Worksheet</h1>

  <div class="task" style="left:25px;top:203px"><span class="task__num">01</span><span class="task__label">GIAE PRE MAIO PERATUR IONSENDEBIS UT IONSENDEBIS</span><span class="task__lines"></span></div>
  <div class="task" style="left:25px;top:288px"><span class="task__num">02</span><span class="task__label">GIAE PRE MAIO PERATUR IONSENDEBIS UT IONSENDEBIS</span><span class="task__lines"></span></div>
  <div class="task" style="left:25px;top:372px"><span class="task__num">03</span><span class="task__label">GIAE PRE MAIO PERATUR IONSENDEBIS UT IONSENDEBIS</span><span class="task__lines"></span></div>
  <div class="task" style="left:25px;top:456px"><span class="task__num">04</span><span class="task__label">GIAE PRE MAIO PERATUR IONSENDEBIS UT IONSENDEBIS</span><span class="task__lines"></span></div>
  <div class="task" style="left:429px;top:203px"><span class="task__num">05</span><span class="task__label">GIAE PRE MAIO PERATUR IONSENDEBIS UT IONSENDEBIS</span><span class="task__lines"></span></div>
  <div class="task" style="left:429px;top:288px"><span class="task__num">06</span><span class="task__label">GIAE PRE MAIO PERATUR IONSENDEBIS UT IONSENDEBIS</span><span class="task__lines"></span></div>
  <div class="task" style="left:429px;top:372px"><span class="task__num">07</span><span class="task__label">GIAE PRE MAIO PERATUR IONSENDEBIS UT IONSENDEBIS</span><span class="task__lines"></span></div>
  <div class="task" style="left:429px;top:456px"><span class="task__num">08</span><span class="task__label">GIAE PRE MAIO PERATUR IONSENDEBIS UT IONSENDEBIS</span><span class="task__lines"></span></div>

  <footer class="footer footer--left"><span>14</span><span class="footer__dot"></span><span class="footer__name">The Coastal Brightpath Centre</span></footer>
  <footer class="footer footer--right"><span class="footer__name">The Coastal Brightpath Centre</span><span class="footer__dot"></span><span>15</span></footer>
</section>

<section class="spread spread--questions">
  <div class="wood" role="img" aria-label="Wooden table top framed with fresh vegetables: tomato, carrots, parsley, cucumber and green pepper"></div>
  <header class="masthead">
    <span class="masthead__name">The Coastal Brightpath Centre for Skills and Learning</span>
    <span class="masthead__rule"></span>
    <span class="masthead__edition">EDITION 1 | 2018</span>
  </header>
  <h1 class="title title--questions">Question and Reflections</h1>

  <svg width="0" height="0" style="position:absolute">
    <defs>
      <symbol id="person" viewBox="0 0 48 62">
        <ellipse cx="23" cy="24" rx="10" ry="13" fill="#fff"/>
        <path d="M4 62 C5 48 14 43 23 42 C32 43 41 48 42 62 Z" fill="#fff"/>
      </symbol>
    </defs>
  </svg>

  <div class="answer" style="left:22px;top:156px"><svg class="answer__icon"><use href="#person"/></svg><span class="answer__lines"></span></div>
  <div class="answer" style="left:22px;top:230px"><svg class="answer__icon"><use href="#person"/></svg><span class="answer__lines"></span></div>
  <div class="answer" style="left:22px;top:305px"><svg class="answer__icon"><use href="#person"/></svg><span class="answer__lines"></span></div>
  <div class="answer" style="left:22px;top:381px"><svg class="answer__icon"><use href="#person"/></svg><span class="answer__lines"></span></div>
  <div class="answer" style="left:22px;top:457px"><svg class="answer__icon"><use href="#person"/></svg><span class="answer__lines"></span></div>
  <div class="answer" style="left:426px;top:156px"><svg class="answer__icon"><use href="#person"/></svg><span class="answer__lines"></span></div>
  <div class="answer" style="left:426px;top:230px"><svg class="answer__icon"><use href="#person"/></svg><span class="answer__lines"></span></div>
  <div class="answer" style="left:426px;top:305px"><svg class="answer__icon"><use href="#person"/></svg><span class="answer__lines"></span></div>
  <div class="answer" style="left:426px;top:381px"><svg class="answer__icon"><use href="#person"/></svg><span class="answer__lines"></span></div>
  <div class="answer" style="left:426px;top:457px"><svg class="answer__icon"><use href="#person"/></svg><span class="answer__lines"></span></div>

  <footer class="footer footer--left"><span>16</span><span class="footer__dot"></span><span class="footer__name">The Coastal Brightpath Centre</span></footer>
  <footer class="footer footer--right"><span class="footer__name">The Coastal Brightpath Centre</span><span class="footer__dot"></span><span>17</span></footer>
</section>

</body>
</html>
```